Vorla Pty Ltd business card design

We need a business card for our company who is involved in upper market residential property development.
Design should be elegant and contemporary.

Our residences are inspired and elegant in contemporary design, combined with inviting ambience. We produce exclusive boutique developments which appeal to the most discerning of purchasers.
We would like to see a design to reflect the above.

Industry/Entity Type

Residential

Contact Information for Business Card

Vorla Pty Ltd, Marek Dunsworth, PO Box 58 Kelvale 3194 Melbourne AUSTRALIA, ph (+61 3) 0427 5926 84

Logo Text

Vorla Pty Ltd

```html
<!DOCTYPE html>
<html lang="en">
<head>
<meta charset="utf-8">
<title>Vorla Pty Ltd — Business Card</title>
<link rel="stylesheet" href="https://fonts.googleapis.com/css2?family=Open+Sans:wght@300;400;600&family=Oswald:wght@400;500&display=swap">
<style>
  :root {
    --canvas: #f1efec;
    --card: #2b2b2c;
    --card-edge: #1f1f20;
    --band: #f4f4f2;
    --band-shade: #dcdcda;
    --accent: #2aa3d8;
    --label: #25a9d8;
    --text-light: #d2d2d2;
    --text-dim: #a3a3a3;
  }
  * { box-sizing: border-box; margin: 0; padding: 0; }
  html, body {
    width: 849px; height: 1200px; overflow: hidden;
    background: var(--canvas);
  }
  .sheet { position: relative; width: 849px; height: 1200px; }
  .side-label {
    position: absolute; right: 74px;
    font-family: "Oswald", "Arial Narrow", sans-serif;
    font-size: 44px; letter-spacing: 1px; color: var(--label);
  }
  .side-label--front { top: 40px; }
  .side-label--back { top: 640px; }
  .card {
    position: absolute; left: 74px; width: 700px; height: 428px;
    background: var(--card);
    border-radius: 4px;
    box-shadow: 0 10px 24px rgba(0,0,0,0.22), 0 0 0 1px var(--card-edge);
    overflow: hidden;
  }
  .card--front { top: 120px; }
  .card--back { top: 720px; }
  .card__band { position: absolute; inset: 0; width: 700px; height: 428px; }
  .band-fill { fill: var(--band); }
  .band-shade { fill: var(--band-shade); }

  .brand-name {
    position: absolute;
    font-family: "Oswald", "Arial Narrow", sans-serif;
    font-weight: 500; color: var(--accent);
    line-height: 1; white-space: nowrap;
  }
  .brand-name--front {
    left: 0; right: 0; top: 196px; text-align: center;
    font-size: 50px; letter-spacing: 3px;
    transform: rotate(-4deg);
  }
  .brand-name--back {
    left: 70px; top: 92px;
    font-size: 36px; letter-spacing: 2px;
    transform: rotate(-15deg); transform-origin: left center;
  }

  .back-details {
    position: absolute; left: 300px; top: 200px;
    font-family: "Open Sans", Arial, sans-serif;
  }
  .back-details__company {
    font-size: 40px; font-weight: 300; color: var(--accent);
    margin-bottom: 22px; line-height: 1;
  }
  .back-details__person {
    font-size: 17px; font-weight: 600; color: var(--text-light);
    margin-bottom: 4px;
  }
  .back-details__line {
    font-size: 15px; font-weight: 400; color: var(--text-dim);
    line-height: 1.6;
  }
</style>
</head>
<body>
  <main class="sheet">
    <div class="side-label side-label--front">FRONT</div>
    <section class="card card--front" aria-label="Card front">
      <svg class="card__band" viewBox="0 0 700 428" aria-hidden="true">
        <polygon class="band-shade" points="0,300 700,250 700,262 0,312"/>
        <polygon class="band-fill" points="0,180 700,130 700,250 0,300"/>
      </svg>
      <div class="brand-name brand-name--front">VORLA PTY LTD</div>
    </section>

    <div class="side-label side-label--back">BACK</div>
    <section class="card card--back" aria-label="Card back">
      <svg class="card__band" viewBox="0 0 700 428" aria-hidden="true">
        <polygon class="band-shade" points="0,250 700,0 700,12 0,262"/>
        <polygon class="band-fill" points="0,60 460,0 700,0 0,250"/>
      </svg>
      <div class="brand-name brand-name--back">VORLA PTY LTD</div>
      <div class="back-details">
        <p class="back-details__company">Vorla Pty Ltd</p>
        <p class="back-details__person">Marek Dunsworth</p>
        <p class="back-details__line">PO Box 58 Kelvale 3194</p>
        <p class="back-details__line">Melbourne AUSTRALIA</p>
        <p class="back-details__line">ph (+61 3) 0427 5926 84</p>
      </div>
    </section>
  </main>
</body>
</html>
```